Bref créative
Brant & Co. LLC
Commercial Real Estate/ Invesment Group/Commercial Investment Group
Simple
Thomas Verhoeven
Aquisitions/Development
Not needed
555-318-2096 not on stationary
tom@brantandcollc.example
brantandcollc.example

```html
<!DOCTYPE html>
<html lang="en">
<head>
<meta charset="utf-8">
<title>Brant &amp; Co. LLC — Business Card</title>
<link rel="stylesheet" href="https://fonts.googleapis.com/css2?family=PT+Sans:wght@400;700&display=swap">
<style>
  :root {
    --backdrop: #e9e6e1;
    --card: #ffffff;
    --gold: #c29a3a;
    --gold-light: #e2c77c;
    --gold-dark: #a47c25;
    --silver: #c9c9cb;
    --silver-light: #ececee;
    --ink: #222222;
    --grey-text: #6b6b6b;
    --rule: #9a9a9a;
  }
  html, body {
    margin: 0;
    width: 1200px;
    height: 944px;
    overflow: hidden;
    background: var(--backdrop);
  }
  .business-card {
    position: absolute;
    left: 100px;
    top: 186px;
    width: 1000px;
    height: 572px;
    background: var(--card);
    border-radius: 44px;
    overflow: hidden;
    box-shadow: 0 18px 40px rgba(0,0,0,0.18);
  }
  .brand {
    position: absolute;
    left: 80px;
    top: 86px;
    display: flex;
    align-items: center;
    gap: 26px;
  }
  .brand-mark {
    width: 84px;
    height: 84px;
    background: var(--gold);
  }
  .brand-name {
    font-family: "PT Sans", sans-serif;
    font-weight: 700;
    font-size: 66px;
    line-height: 1;
    color: var(--gold);
  }
  .holder {
    position: absolute;
    right: 620px;
    top: 292px;
    text-align: right;
    font-family: "PT Sans", sans-serif;
  }
  .holder-name {
    font-weight: 700;
    font-size: 34px;
    color: var(--gold);
  }
  .holder-role {
    font-weight: 700;
    font-size: 20px;
    color: var(--ink);
    margin-top: 4px;
  }
  .divider {
    position: absolute;
    left: 400px;
    top: 238px;
    width: 2px;
    height: 150px;
    background: var(--rule);
  }
  .contact-list {
    position: absolute;
    left: 424px;
    top: 236px;
    margin: 0;
    padding: 0;
    list-style: none;
    font-family: "PT Sans", sans-serif;
    font-size: 25px;
    line-height: 30px;
    color: var(--grey-text);
  }
  .footer-band {
    position: absolute;
    left: 0;
    bottom: 0;
    width: 1000px;
    height: 200px;
  }
</style>
</head>
<body>
  <div class="business-card">
    <div class="brand">
      <div class="brand-mark"></div>
      <span class="brand-name">Brant &amp; Co. LLC</span>
    </div>

    <div class="holder">
      <div class="holder-name">Thomas Verhoeven</div>
      <div class="holder-role">Aquisitions/Development</div>
    </div>

    <div class="divider"></div>

    <ul class="contact-list">
      <li>Phone: 555-318-2040</li>
      <li>Cell: 555-318-2096</li>
      <li>Fax: 555-318-2077</li>
      <li>Email : tom@brantandcollc.example</li>
      <li>Web : www.brantandcollc.example</li>
    </ul>

    <svg class="footer-band" viewBox="0 0 1000 200" preserveAspectRatio="none">
      <defs>
        <linearGradient id="silverSweep" x1="0" y1="0" x2="1" y2="0">
          <stop offset="0" stop-color="var(--silver-light)"/>
          <stop offset="0.6" stop-color="var(--silver)"/>
          <stop offset="1" stop-color="var(--silver-light)"/>
        </linearGradient>
        <linearGradient id="goldSweep" x1="0" y1="0" x2="1" y2="0">
          <stop offset="0" stop-color="var(--gold-dark)"/>
          <stop offset="0.35" stop-color="var(--gold-light)"/>
          <stop offset="0.7" stop-color="var(--gold)"/>
          <stop offset="1" stop-color="var(--gold-dark)"/>
        </linearGradient>
      </defs>
      <path d="M0 70 C 260 110, 620 90, 1000 28 L1000 200 L0 200 Z" fill="url(#silverSweep)"/>
      <path d="M0 96 C 280 130, 640 112, 1000 56 L1000 200 L0 200 Z" fill="url(#goldSweep)"/>
    </svg>
  </div>
</body>
</html>
```